Corona rapid test station

We need a banner for a container. This container will stand in the pedestrian zone of a large city. What is required is high-quality graphics with pictures of people who draw the eye, but also fit the topic of the Corona rapid test. One possible theme is the portrayal of young people getting tested to protect their older relatives.

Corona rapid test, result within 15 minutes
Pre-registration by phone: 0648/27 584 6

Leave empty field for price.

The umbrella brand should be clearly visible: Lindwurm-Apotheken (Attention, an n must be added to the existing logo: Lindwurm-Apotheken <-)

The branches are to be listed smaller: Lindwurm-Apotheke, Erl-Apotheke, Quastel-Apotheke, Brigam-Apotheke

Format: 2m high, 5.5m wide

Target Market(s)

People between 20 and 60 years of age

Requirements
Must have
• The logo of the umbrella brand Lindwurm-Apotheken stands above everything. The design of the central pharmacies (green / blue) is reflected in the overall design.
Font Nexa Bold or Nexa light
Nice to have
• Faces of people without a mask

```html
<!DOCTYPE html>
<html lang="de">
<head>
<meta charset="utf-8">
<title>Lindwurm-Apotheken – Corona Schnelltest Banner</title>
<link rel="stylesheet" href="https://fonts.googleapis.com/css2?family=Montserrat:wght@700&family=Questrial&display=swap">
<style>
  :root {
    --navy: #1f3660;
    --green: #5fb84a;
    --pale: #eef0c8;
    --white: #ffffff;
    --photo-hair: #9c7458;
    --photo-skin: #e3c3b0;
    --photo-shirt: #9fbde0;
    --photo-back: #dcdcd8;
    --page: #ffffff;
  }
  html, body {
    margin: 0;
    padding: 0;
    width: 1200px;
    height: 752px;
    overflow: hidden;
    background: var(--page);
  }
  .canvas {
    position: relative;
    width: 1200px;
    height: 752px;
  }
  .banner {
    position: absolute;
    left: 134px;
    top: 144px;
    width: 938px;
    height: 468px;
    overflow: hidden;
    box-shadow: 0 6px 10px rgba(0, 0, 0, 0.22);
  }
  .banner-shapes {
    position: absolute;
    inset: 0;
  }
  .headline {
    position: absolute;
    left: 17px;
    top: 131px;
    margin: 0;
    font-family: "Montserrat", sans-serif;
    font-weight: 700;
    font-size: 18.5px;
    line-height: 32.5px;
    letter-spacing: -0.5px;
    color: var(--green);
    text-transform: uppercase;
  }
  .branches {
    position: absolute;
    left: 17px;
    top: 244px;
    margin: 0;
    padding: 0;
    list-style: none;
    font-family: "Questrial", sans-serif;
    font-size: 18.5px;
    line-height: 28.2px;
    color: var(--pale);
  }
  .branches li::before {
    content: "•";
    font-size: 12px;
    margin-right: 5px;
    vertical-align: 2px;
  }
  .price-badge {
    position: absolute;
    left: 421px;
    top: 280px;
    width: 80px;
    height: 80px;
    border-radius: 50%;
    background: var(--white);
    box-shadow: 1px 2px 3px rgba(0, 0, 0, 0.25);
    display: flex;
    align-items: center;
    justify-content: center;
    font-family: "Montserrat", sans-serif;
    font-weight: 700;
    font-size: 24px;
    color: var(--green);
  }
  .price-badge .dots {
    font-size: 16px;
    margin-right: 6px;
  }
  .brand {
    position: absolute;
    right: 22px;
    top: 74px;
    display: flex;
    align-items: center;
    gap: 7px;
    font-family: "Montserrat", sans-serif;
    font-weight: 700;
    font-size: 17px;
    letter-spacing: 0.5px;
    color: var(--navy);
  }
  .brand-dot {
    width: 12px;
    height: 12px;
    border-radius: 50%;
    background: var(--green);
  }
</style>
</head>
<body>
<div class="canvas">
  <section class="banner">
    <svg class="banner-shapes" width="938" height="468" viewBox="0 0 938 468">
      <defs>
        <linearGradient id="photoTone" x1="0.1" y1="0" x2="0.55" y2="1">
          <stop offset="0" stop-color="var(--photo-hair)"/>
          <stop offset="0.35" stop-color="var(--photo-skin)"/>
          <stop offset="0.7" stop-color="var(--photo-shirt)"/>
          <stop offset="1" stop-color="var(--photo-back)"/>
        </linearGradient>
        <clipPath id="stripeZone">
          <rect x="0" y="178" width="938" height="290"/>
        </clipPath>
      </defs>
      <rect class="photo-area" x="380" y="0" width="558" height="468" fill="url(#photoTone)" role="img" aria-label="Photo: smiling young woman in a light blue T-shirt getting a quick test at the upper arm from a gloved hand"/>
      <path class="accent-stripe" clip-path="url(#stripeZone)" d="M0 0 H469 C500 60 520 120 512 175 C505 260 450 360 414 468 H0 Z" fill="var(--green)"/>
      <path class="navy-field" d="M0 0 H459 C490 60 510 120 502 175 C495 260 440 360 404 468 H0 Z" fill="var(--navy)"/>
    </svg>

    <div class="brand">
      <span class="brand-dot"></span>
      <span class="brand-name">Lindwurm-Apotheken</span>
    </div>

    <p class="headline">Corona rapid test, result within 15 minutes<br>Pre-registration by phone: 0648/27 584 6</p>

    <ul class="branches">
      <li>Lindwurm-Apotheke.</li>
      <li>Erl-Apotheke.</li>
      <li>Quastel-Apotheke.</li>
      <li>Brigam-Apotheke.</li>
    </ul>

    <div class="price-badge"><span class="dots">...</span><span class="currency">$</span></div>
  </section>
</div>
</body>
</html>
```